4 Banners for homepage and logo

Logo for SiteTitleCounsel.net and 4 banners for the center of the page.

Logo should be clean and pretty basic.

Banners
1.
Domain Name Disputes
We'll recover your domain names, Guaranteed or its free!

2.
Reputation management
We get defamatory content removed from Quorvix, Brindle, Chatterloom, and Pallbook!

3.
Domain name management
Create an offensive or defensive domain name strategy for your company

4.
Defensive reputation management
Get ahead of the game and make your image shine online!

```html
<!DOCTYPE html>
<html lang="en">
<head>
<meta charset="utf-8">
<title>Defensive reputation management</title>
<link rel="stylesheet" href="https://fonts.googleapis.com/css2?family=Arimo:wght@700&family=Roboto+Condensed:wght@700&display=swap">
<style>
  :root {
    --bg: #ffffff;
    --alert-fill: #f9c8c0;
    --alert-stroke: #e8543c;
    --icon-red: #d9414a;
    --icon-ring: #f3b1b4;
    --text: #4e4e4e;
    --close: #e8543c;
    --pill-stroke: #f6cdc6;
    --pill-fill: #ffffff;
  }
  html, body {
    margin: 0;
    padding: 0;
    width: 1200px;
    height: 900px;
    overflow: hidden;
    background: var(--bg);
  }
  .banner {
    position: relative;
    width: 1200px;
    height: 900px;
  }
  .alert-shape {
    position: absolute;
    left: 0;
    top: 0;
  }
  .alert-icon {
    position: absolute;
    left: 42px;
    top: 100px;
  }
  .alert-title {
    position: absolute;
    left: 150px;
    top: 148px;
    margin: 0;
    font-family: "Roboto Condensed", "Arial Narrow", sans-serif;
    font-weight: 700;
    font-size: 50px;
    line-height: 1;
    color: var(--text);
    letter-spacing: -0.5px;
  }
  .alert-close {
    position: absolute;
    left: 1144px;
    top: 90px;
    font-family: Arimo, Arial, sans-serif;
    font-size: 24px;
    color: var(--close);
    font-weight: 400;
  }
  .tagline {
    position: absolute;
    left: 120px;
    top: 624px;
    width: 1040px;
    height: 222px;
    box-sizing: border-box;
    border: 9px solid var(--pill-stroke);
    border-radius: 48px;
    background: var(--pill-fill);
    display: flex;
    align-items: center;
    justify-content: center;
  }
  .tagline-text {
    margin: 0;
    font-family: "Roboto Condensed", "Arial Narrow", sans-serif;
    font-weight: 700;
    font-size: 50px;
    color: var(--text);
    letter-spacing: -0.5px;
  }
</style>
</head>
<body>
  <main class="banner">
    <svg class="alert-shape" width="1200" height="420" viewBox="0 0 1200 420" aria-hidden="true">
      <path d="M40 56 H1152 Q1172 56 1172 76 V298 Q1172 318 1152 318 H150 L168 392 L130 318 H40 Q20 318 20 298 V76 Q20 56 40 56 Z"
            fill="var(--alert-fill)" stroke="var(--alert-stroke)" stroke-width="3"/>
    </svg>
    <svg class="alert-icon" width="80" height="178" viewBox="0 0 80 178" aria-hidden="true">
      <ellipse cx="40" cy="89" rx="38" ry="87" fill="var(--icon-ring)"/>
      <ellipse cx="40" cy="89" rx="32" ry="80" fill="var(--icon-red)"/>
      <path d="M24 60 L56 118 M56 60 L24 118" stroke="#ffffff" stroke-width="12" stroke-linecap="round"/>
    </svg>
    <h1 class="alert-title">Defensive reputation management!</h1>
    <span class="alert-close">x</span>
    <div class="tagline">
      <p class="tagline-text">Get ahead of the game and make your image shine online!</p>
    </div>
  </main>
</body>
</html>
```